Website for Franchise Builder

We are a web design and Architectural company that is selling an all in one Business solution for small to medium size builders.

We are Frame KV.

We are providing builders with the following services:

1. Dynamic Site quarry websites and Tavrone Apps
2. Rebranded housed plans with Brochures
3. Logo and Corporate identity
4. Estimating software
5. 3d Visualisation and Rendering
5. Building design and Planning support.

We will be helping builders to complete and have a competitive edge against the large franchise building companies. Who control the House building market in Australia. The large companies have great website, apps, brochures and standard house plans. So that is exactly what we will be providing our builders. At a fraction of the normal cost. We will have help them to win jobs and look more professional.

My current website is:

http://norvellpage.sitequarry.com

I have attached and provided the following:

1. whole website Mock-up
2. Separated competition Pages to mock-up
2. Logo (in latest advertisement zip file)
4. Images and that my be useful
5. Some information on our services
6. Latest magazine advertisement (notice the ad also displays the roofdraftguild. Which is a separate website that sells our house plans)

The five pages i would like designed for the competition are follows:

1. Home Page
2. What we do - Websites & Tavrone Apps
3. How it works
4. Our work - Display individual websites similar to the way www.plomarex.com displays their websites
5. Builders packages (pricing table. Mockup has incorrect items for table. See please pdf with correct data for table)

Please use the mock-ups as a guide only. Go for it with your creativity please.

Sites that i really like are:

- www.plomarex.com
- www.quillmarket.com.au

Target Market(s)

Builders and Wifes of Builders

Industry/Entity Type

Business

Requirements
Must have
• 1. Testimonails displayed on home page somewhere
2. Social media on home page, and on individual pages displaying websites

Nice to have
• I really like the www.plomarex.com. The way they use icons and have the catch phrases. We could have catch phase such as:

1. All in one Business Solution for builders
2. Lets Get Started View websites
3. Ready to Go Business Solutions for Builders.

```html
<!DOCTYPE html>
<html lang="en">
<head>
<meta charset="utf-8">
<title>Frame KV — Builders IT Solutions</title>
<link rel="stylesheet" href="https://fonts.googleapis.com/css2?family=Roboto+Condensed:wght@400;700&family=Noto+Sans:wght@400&display=swap">
<style>
:root{
  --blue:#0d8fd8;
  --sky:#16b3ec;
  --sky-dark:#0a7fd1;
  --ink:#333;
  --rule:#dcdcdc;
  --nav-top:#f3f3f3;
  --nav-bot:#cfcfcf;
  --link:#6a6a6a;
}
*{box-sizing:border-box;margin:0;padding:0}
html,body{width:1038px;height:1200px;overflow:hidden;background:#fff}
body{position:relative;font-family:"Noto Sans",Verdana,sans-serif;color:var(--ink);font-size:9.4px;line-height:1.6}
.abs{position:absolute}
.header-band{left:0;top:22px;width:1038px;height:200px;background:linear-gradient(#dcdcdc,#f4f4f4 55%,#fff)}
.utility{top:5px;right:225px;font-size:9.6px;color:var(--link)}
.utility span{margin:0 3px}
.social{top:3px;left:818px;display:flex;gap:5px}
.social i{width:16px;height:16px;display:block;border-radius:2px}
.logo{left:163px;top:58px;display:flex;align-items:center;gap:8px}
.logo-name{font-family:"Roboto Condensed",sans-serif;font-weight:700;font-size:34px;color:var(--blue);line-height:1}
.logo-dot{width:22px;height:22px;border-radius:50%;background:var(--sky)}
.tagline{left:163px;top:92px;font-family:"Roboto Condensed",sans-serif;font-size:18px;color:#8a8a8a}
.phone{left:700px;top:40px;font-family:"Roboto Condensed",sans-serif;font-weight:700;font-size:25px;color:var(--sky);letter-spacing:.5px}
.search{left:702px;top:75px;width:161px;height:25px;border:1px solid #ccc;background:#fff;font-size:9.6px;color:#777;padding:4px 6px}
.search svg{position:absolute;right:6px;top:6px}
.nav{left:154px;top:133px;width:730px;height:41px;display:flex;background:linear-gradient(var(--nav-top),var(--nav-bot));border:1px solid #c4c4c4}
.nav a{font-family:"Roboto Condensed",sans-serif;font-size:13px;color:#3a3a3a;text-decoration:none;display:flex;align-items:center;justify-content:center;border-right:1px solid #bdbdbd;text-transform:uppercase;white-space:nowrap}
.nav a:last-child{border-right:0}
.nav a.active{background:linear-gradient(var(--sky),var(--sky-dark));color:#fff}
.headline{left:0;width:1038px;top:196px;text-align:center;font-family:"Roboto Condensed",sans-serif;font-size:15.5px;color:var(--blue)}
.slide{background:#ccc;padding:7px;box-shadow:0 8px 14px rgba(0,0,0,.12)}
.slide div{width:100%;height:100%}
.arrow{width:35px;height:35px}
.section-title{left:0;width:1038px;top:527px;text-align:center;font-family:"Roboto Condensed",sans-serif;font-size:13.5px;color:#444}
.rule{height:1px;background:var(--rule)}
.intro{left:160px;width:718px;top:562px;text-align:center;color:#333}
.box-head{background:var(--sky);color:#fff;font-family:"Roboto Condensed",sans-serif;font-size:13.5px;padding:7px 9px;line-height:1.15}
.box{border:1px solid #ddd;background:#fff;box-shadow:0 8px 10px -6px rgba(0,0,0,.15)}
.quote{padding:12px 10px 0 11px;text-align:justify}
.quote b{font-family:Georgia,serif;font-size:26px;color:#ccc;line-height:0;vertical-align:-8px;margin-right:2px}
.person{display:flex;gap:8px;align-items:center;padding:8px 11px}
.avatar{width:36px;height:34px;background:linear-gradient(#6d4a35,#3a2a22)}
.service{width:241px}
.service h3{font-family:"Roboto Condensed",sans-serif;font-weight:400;font-size:12px;color:#444;text-transform:uppercase;padding-bottom:6px;border-bottom:1px solid var(--rule)}
.service .body{display:flex;gap:8px;margin-top:8px}
.service .icon{flex:0 0 64px;height:60px;border-radius:8px}
.service p{text-align:justify}
.enquiry{left:0;width:1038px;top:1091px;display:flex;justify-content:center;align-items:center;gap:8px;font-family:"Roboto Condensed",sans-serif;font-size:11px;color:#444}
.enquiry a{background:linear-gradient(var(--sky),var(--sky-dark));color:#fff;font-size:14px;padding:5px 18px;text-decoration:none}
.footer-links{left:0;width:1038px;top:1147px;text-align:center;color:#888;font-size:9.6px}
.copy{left:0;width:1038px;top:1167px;text-align:center;color:#888;font-size:9.6px}
.copy span{color:var(--blue)}
</style>
</head>
<body>
<div class="abs header-band"></div>

<div class="abs utility">Support <span>|</span> Client Portal <span>|</span> Contact <span>|</span> About <span>|</span> Connect</div>
<div class="abs social"><i style="background:#3b5b99"></i><i style="background:#39b0e4"></i><i style="background:#c4302b"></i></div>

<div class="abs logo"><span class="logo-dot"></span><span class="logo-name">Frame KV</span></div>
<div class="abs tagline">builders IT solutions</div>

<div class="abs phone">1300 555 014</div>
<div class="abs search">Search
  <svg width="12" height="12" viewBox="0 0 12 12"><circle cx="5" cy="5" r="3.5" fill="none" stroke="#bbb" stroke-width="1.4"/><line x1="7.5" y1="7.5" x2="11" y2="11" stroke="#bbb" stroke-width="1.6"/></svg>
</div>

<nav class="abs nav">
  <a class="active" style="width:89px">What we do</a><a style="width:128px">Builders packages</a><a style="width:104px">How it works</a><a style="width:125px">Site quarry</a><a style="width:127px">Support network</a><a style="width:79px">Our work</a><a style="width:76px">Free trail</a>
</nav>

<div class="abs headline">READY TO GO BUSINESS SOLUTIONS FOR BUILDERS?</div>

<div class="abs slide" style="left:187px;top:265px;width:96px;height:208px"><div role="img" aria-label="House with veranda and lawn" style="background:linear-gradient(#8fa7d9,#5d7a45 55%,#3f6b2a)"></div></div>
<div class="abs slide" style="left:796px;top:265px;width:57px;height:208px"><div role="img" aria-label="Brick house facade with garden" style="background:linear-gradient(#8fa7d9,#555 45%,#5b7a3e)"></div></div>
<div class="abs slide" style="left:269px;top:250px;width:100px;height:235px"><div role="img" aria-label="House side wall and driveway" style="background:linear-gradient(#7d9ad8,#d8d4cc 50%,#55667e)"></div></div>
<div class="abs slide" style="left:680px;top:250px;width:92px;height:235px"><div role="img" aria-label="Modern house with trees" style="background:linear-gradient(#7d9ad8,#cfcac0 50%,#4f7a33)"></div></div>
<div class="abs slide" style="left:351px;top:235px;width:336px;height:262px"><div role="img" aria-label="Front of a new brick family home with garden path" style="background:linear-gradient(#7f9fe0,#aec3ee 35%,#4b5b78 48%,#9a8e86 62%,#3d6b2c 82%,#5d6f8c)"></div></div>

<svg class="abs arrow" style="left:172px;top:353px" viewBox="0 0 35 35"><circle cx="17.5" cy="17.5" r="17.5" fill="#1b1b1b"/><path d="M19 12l-6 5.5 6 5.5M24 12l-6 5.5 6 5.5" fill="none" stroke="#fff" stroke-width="2"/></svg>
<svg class="abs arrow" style="left:832px;top:353px" viewBox="0 0 35 35"><circle cx="17.5" cy="17.5" r="17.5" fill="#1b1b1b"/><path d="M11 12l6 5.5-6 5.5M16 12l6 5.5-6 5.5" fill="none" stroke="#fff" stroke-width="2"/></svg>

<div class="abs section-title">WHAT WE DO?</div>
<div class="abs rule" style="left:158px;top:552px;width:724px"></div>
<p class="abs intro">Nulla auctor, lectus tristique dignissim bibendum, elit augue sodales felis, porta molestie sem mi vitae nisi. Nulla justo enim, fringilla vel gravida id, ullamcorper id enim. Cum sociis natoque penatibus et magnis dis parturient montes, nascetur ridiculus mus. Nam volutpat fermentum enim, et cursus lectus mattis id. Duis scelerisque, dui et pellentesque accumsan, metus nulla pretium erat, non vehicula velit velit in ante.</p>

<div class="abs box" style="left:154px;top:634px;width:194px;height:186px">
  <div class="box-head">TESTIMONIALS</div>
  <p class="quote"><b>“</b>Nunc convallis odio dignissim enim dictum fringilla. Nam faucibus pharetra lectus, eu faucibus ligula posuere in. Nulla facilisi. Quisque pellentesque velit eget neque viverra non iaculis ante mollis.</p>
  <div class="person"><div class="avatar" role="img" aria-label="Client portrait"></div><div>Dana Corliss<br>MD, Veltrano</div></div>
</div>

<div class="abs box" style="left:154px;top:850px;width:196px;height:195px">
  <div class="box-head">WHAT THIS VIDEO ON YOUR WEBSITE</div>
  <div role="img" aria-label="Video of a 3D house model over building plans" style="margin:8px 7px;height:126px;border:1px solid #ccc;background:linear-gradient(135deg,#f2f2f2,#bdbdbd 45%,#8a6a50 70%,#e8e8e8);position:relative">
    <div style="position:absolute;left:0;right:0;bottom:0;height:10px;background:#222"></div>
  </div>
</div>

<div class="abs service" style="left:370px;top:634px"><h3>Online marketing &amp; social media</h3><div class="body"><div class="icon" role="img" aria-label="Group of networked people figures" style="background:linear-gradient(135deg,#e8c23a,#d23b2b 50%,#2a8a3a)"></div><p>Maecenas molestie adipiscing lacinia. Quisque consequat sollicitudin enim, nec ullamcorper quam iaculis id. Nullam massa turpis.</p></div></div>
<div class="abs service" style="left:626px;top:634px"><h3>Completely rebrandable house plans</h3><div class="body"><div class="icon" role="img" aria-label="Small house illustration" style="background:linear-gradient(#f4ecd0,#b8b08a)"></div><p>Maecenas molestie adipiscing lacinia. Quisque consequat sollicitudin enim, nec ullamcorper quam iaculis id. Nullam massa turpis.</p></div></div>

<div class="abs service" style="left:370px;top:739px"><h3>Construction estimating software</h3><div class="body"><div class="icon" role="img" aria-label="Software box illustration" style="background:linear-gradient(#c86a4a,#6a86a8)"></div><p>Quisque consequat sollicitudin enim, nec ullamcorper quam iaculis id. Nullam massa turpis. Maecenas molestie adipiscing lacinia.</p></div></div>
<div class="abs service" style="left:626px;top:739px"><h3>Awesome support 24/7</h3><div class="body"><div class="icon" role="img" aria-label="Support agent with headset" style="background:linear-gradient(#e8a860,#7a4a3a)"></div><p>Quisque consequat sollicitudin enim, nec ullamcorper quam iaculis id. Nullam massa turpis. Maecenas molestie adipiscing lacinia.</p></div></div>

<div class="abs service" style="left:370px;top:848px"><h3>Websites &amp; Tavrone apps</h3><div class="body"><div class="icon" role="img" aria-label="Mobile phone showing a city" style="background:linear-gradient(#1a2440,#5a3a6a)"></div><p>Quisque consequat sollicitudin enim, nec ullamcorper quam iaculis id. Nullam massa turpis. Maecenas molestie adipiscing lacinia.</p></div></div>
<div class="abs service" style="left:626px;top:848px"><h3>Branding &amp; logo</h3><div class="body"><div class="icon" role="img" aria-label="Branding materials and disc" style="background:linear-gradient(#e4e8f4,#9aa4c0)"></div><p>Quisque consequat sollicitudin enim, nec ullamcorper quam iaculis id. Nullam massa turpis. Maecenas molestie adipiscing lacinia.</p></div></div>

<div class="abs service" style="left:370px;top:959px"><h3>Planning and building design</h3><div class="body"><div class="icon" role="img" aria-label="Drafting pencil and ruler" style="background:linear-gradient(135deg,#4a8ad8,#a8c8ea)"></div><p>Ullamcorper quam iaculis id. Nullam massa turpis. Maecenas molestie adipiscing lacinia. Quisque consequat sollicitudin enim, nec</p></div></div>
<div class="abs service" style="left:626px;top:959px"><h3>3D visualisation &amp; rendering</h3><div class="body"><div class="icon" role="img" aria-label="3D cube, cylinder and cone shapes" style="background:linear-gradient(135deg,#e8642a,#3a7ad8 55%,#8ac04a)"></div><p>Ullamcorper quam iaculis id. Nullam massa turpis. Maecenas molestie adipiscing lacinia. Quisque consequat sollicitudin enim, nec</p></div></div>

<div class="abs rule" style="left:158px;top:1078px;width:724px"></div>
<div class="abs enquiry">I am interested in giving my business the competitive edge <a>SEND ENQUIRY</a></div>
<div class="abs rule" style="left:158px;top:1129px;width:724px"></div>

<div class="abs footer-links">Home | What we Do | Builders Packages | How it Works | Site quarry | Support Network | Our Work | Free Trail | Contact Us</div>
<div class="abs copy">© 2012 <span>Frame KV</span> All Rights Reserved. Privacy Policy | Terms and Conditions</div>
</body>
</html>
```